BrookhavenLLC

Real Estate Investment. Buy/Sell house/investment . Trustworthy,Reliable, and friendly

Industry/Entity Type

Real Estate

Contact Information for Business Card

Brookhaven@mailbox-example.com
808-555-0143
Linnea-Joy Patterson

```html
<!DOCTYPE html>
<html lang="en">
<head>
<meta charset="utf-8">
<title>Brookhaven LLC – Business Card</title>
<link rel="stylesheet" href="https://fonts.googleapis.com/css2?family=Cinzel:wght@400&family=Bebas+Neue&family=Questrial&display=swap">
<style>
  :root {
    --brand-blue: #1f78c1;
    --band-blue: #1068a8;
    --card-white: #ffffff;
    --card-shade: #f1f2f3;
    --backdrop: #e4e6e8;
  }
  * { box-sizing: border-box; margin: 0; padding: 0; }
  html, body {
    width: 1200px;
    height: 800px;
    overflow: hidden;
    background: var(--backdrop);
  }
  .business-card {
    position: absolute;
    left: 100px;
    top: 110px;
    width: 1000px;
    height: 580px;
    border-radius: 44px;
    overflow: hidden;
    background: linear-gradient(180deg, var(--card-white) 0%, var(--card-white) 40%, var(--card-shade) 100%);
    box-shadow: 0 6px 18px rgba(0,0,0,0.12);
  }
  .company-name {
    position: absolute;
    left: 0;
    right: 60px;
    top: 120px;
    text-align: center;
    font-family: "Cinzel", serif;
    font-weight: 400;
    font-size: 62px;
    letter-spacing: 3px;
    color: var(--brand-blue);
  }
  .holder-name {
    position: absolute;
    right: 40px;
    top: 270px;
    font-family: "Bebas Neue", sans-serif;
    font-size: 44px;
    letter-spacing: 2px;
    color: var(--brand-blue);
  }
  .divider {
    position: absolute;
    left: 0;
    right: 0;
    top: 322px;
    height: 4px;
    background: var(--brand-blue);
  }
  .contact-list {
    position: absolute;
    left: 78px;
    top: 360px;
    list-style: none;
  }
  .contact-item {
    display: flex;
    align-items: center;
    gap: 22px;
    height: 62px;
    font-family: "Questrial", sans-serif;
    font-size: 32px;
    color: var(--brand-blue);
  }
  .contact-item.phone { letter-spacing: 5px; }
  .contact-item.email { letter-spacing: 0.5px; margin-left: 22px; }
  .contact-icon { width: 46px; height: 46px; flex: none; }
  .bottom-band {
    position: absolute;
    left: 0;
    right: 0;
    bottom: 0;
    height: 60px;
    background: var(--band-blue);
  }
</style>
</head>
<body>
  <div class="business-card">
    <h1 class="company-name">Brookhaven</h1>
    <p class="holder-name">Linnea-Joy Patterson</p>
    <div class="divider"></div>
    <ul class="contact-list">
      <li class="contact-item phone">
        <svg class="contact-icon" viewBox="0 0 46 46" aria-hidden="true">
          <polygon points="23,2 44,17 36,43 10,43 2,17" fill="#1068a8"/>
          <path d="M16 15 q-3 2 -1 7 q3 7 10 10 q5 2 7 -1 l-4 -4 q-2 2 -4 0 q-3 -2 -4 -4 q-2 -2 0 -4 z" fill="#ffffff"/>
        </svg>
        <span>808-555-0143</span>
      </li>
      <li class="contact-item email">
        <svg class="contact-icon" viewBox="0 0 46 46" aria-hidden="true">
          <polygon points="23,2 44,17 36,43 10,43 2,17" fill="#1068a8"/>
          <rect x="11" y="16" width="24" height="16" fill="#ffffff"/>
          <polyline points="11,16 23,26 35,16" fill="none" stroke="#1068a8" stroke-width="2"/>
        </svg>
        <span>Brookhaven@mailbox-example.com</span>
      </li>
    </ul>
    <div class="bottom-band"></div>
  </div>
</body>
</html>
```